Starvu Review Divorce Law Firm Folder Insert

We are a divorce law firm.

We need a flyer just like the one that is posted. For example, that allows for our Starvu reviews to be a good deed. We do like the coloring we will provide the image that goes on the bottom right. We are open to any design. Any thoughts people have, and unique designs are welcome were very happy with this example. However, we want people to know to have some background as to what would be the best option.

Again anything but again we do want the Starvu has to be the five stars in my logo has to be on there and the portion that says these different comments included

Target Market(s)

Divorce and Custody Clients

Industry/Entity Type

Legal

Requirements
Must have
• what must remain is the Starvu logo that large, and the five stars in the front in the back. What must be included is the Starvu reviews listed below. Not all of them must be used but no less than five must be used. At least one of the five

1.) “Worth the money!”
2.) “Simply the best”
3.) “So much knowledge and experience”
4.) “When life gets challenging, you want Marcus on your team!”
5.) “He made a painful divorce and custody, much easier to deal with”
6.) “Willingness to go the extra mile”
7.) “Respectful and caring”
8.) “I wouldn’t go with anyone else!”
Nice to have
• We are a divorce law firm in Harrisburg Pennsylvania. we need a Starvu review insert for our potential new clients folder. We need a hard insert flyer around 6 x 9 in height as similar possible to the one included as an attached, however we are open to any design. Since like the example so much the is a great guidepost.

We appreciate unique designs but have found one we have. To be very much to our liking. We are open to any other signs, but again. One example. Any thoughts people have, and unique designs are welcome were very happy with this example. However, we want people to know to have some background as to what would be the best option.

Attached you will find our logo, our shield by itself, the example card, and three images from which you should pick one.

one possibly to the photos can be included, but not aall three, included are three photos, only one should be used. Please pick one and use it
Should not have
• Look far off of a look that I too crazy

```html
<!DOCTYPE html>
<html lang="en">
<head>
<meta charset="utf-8">
<title>Starvu Review Insert – The Law Office of Marcus R Whitfield</title>
<link rel="stylesheet" href="https://fonts.googleapis.com/css2?family=Lato:ital,wght@0,400;0,700;1,400&family=Arvo:wght@700&display=swap">
<style>
  :root {
    --green-deep: #0f5a26;
    --green-mid: #2a8f45;
    --green-light: #4cb063;
    --quote-dark: #0d3f1c;
    --white: #ffffff;
    --star: #f4a51c;
    --brand-blue: #2f6fd6;
    --wood-dark: #4a1c10;
    --wood-mid: #7b3420;
    --brass: #c9a04a;
  }
  html, body {
    margin: 0;
    padding: 0;
    overflow: hidden;
    background: #e9ece9;
  }
  .insert {
    position: relative;
    width: 800px;
    height: 1200px;
    overflow: hidden;
    font-family: "Lato", sans-serif;
    color: var(--white);
  }
  .hero-photo {
    position: absolute;
    inset: 0;
    background:
      radial-gradient(ellipse at 45% 30%, var(--green-light) 0%, transparent 60%),
      linear-gradient(160deg, var(--green-mid) 0%, var(--green-deep) 55%, #1d7a37 100%);
  }
  .firm-mark {
    position: absolute;
    left: 160px;
    top: 78px;
    display: flex;
    align-items: center;
    gap: 18px;
  }
  .firm-mark__square {
    width: 64px;
    height: 64px;
    background: var(--white);
    opacity: 0.9;
  }
  .firm-mark__name {
    font-weight: 400;
    color: var(--white);
    text-transform: uppercase;
    line-height: 1.05;
    letter-spacing: 1px;
  }
  .firm-mark__small { display: block; font-size: 16px; }
  .firm-mark__large { display: block; font-size: 32px; }

  .review-list {
    position: absolute;
    left: 160px;
    top: 215px;
    margin: 0;
    padding: 0;
    list-style: none;
  }
  .review-list__item {
    display: flex;
    align-items: center;
    gap: 14px;
    font-size: 30px;
    font-style: italic;
    line-height: 1.2;
    margin-bottom: 34px;
  }
  .review-list__stars { flex: none; }

  .testimonial {
    position: absolute;
    right: 38px;
    top: 548px;
    margin: 0;
    text-align: right;
    font-style: italic;
    line-height: 1;
  }
  .testimonial__line {
    display: block;
    font-size: 62px;
    font-weight: 400;
    letter-spacing: -1px;
    margin-bottom: 10px;
  }
  .testimonial__line--accent {
    font-family: "Arvo", serif;
    font-style: normal;
    font-weight: 700;
    color: var(--quote-dark);
    font-size: 66px;
  }
  .review-badge {
    position: absolute;
    right: 40px;
    top: 850px;
  }
  .review-badge__name {
    font-weight: 700;
    font-size: 66px;
    color: var(--brand-blue);
    line-height: 1;
    display: block;
  }
  .review-badge__row {
    display: flex;
    align-items: center;
    gap: 10px;
    margin-top: 4px;
  }
  .review-badge__label {
    font-size: 26px;
    font-weight: 700;
  }
  .gavel-art {
    position: absolute;
    left: 0;
    bottom: 0;
    width: 440px;
    height: 370px;
    background: linear-gradient(160deg, var(--wood-mid) 0%, var(--wood-dark) 60%, var(--brass) 100%);
    border-top-right-radius: 120px;
    opacity: 0.95;
  }
</style>
</head>
<body>
  <main class="insert">
    <svg width="0" height="0" style="position:absolute" aria-hidden="true">
      <defs>
        <polygon id="star" points="12,1 15,9 23,9 16.5,14 19,22 12,17 5,22 7.5,14 1,9 9,9" fill="#f4a51c"/>
      </defs>
    </svg>

    <div class="hero-photo" role="img" aria-label="Attorney in a suit adjusting his jacket, shown under a green tint"></div>

    <header class="firm-mark">
      <div class="firm-mark__square"></div>
      <div class="firm-mark__name">
        <span class="firm-mark__small">The Law Office of</span>
        <span class="firm-mark__large">Marcus R Whitfield</span>
      </div>
    </header>

    <ul class="review-list">
      <li class="review-list__item">
        <svg class="review-list__stars" width="96" height="20" viewBox="0 0 120 24" aria-label="Five stars"><use href="#star" x="0"/><use href="#star" x="24"/><use href="#star" x="48"/><use href="#star" x="72"/><use href="#star" x="96"/></svg>
        “Worth the money!”
      </li>
      <li class="review-list__item">
        <svg class="review-list__stars" width="96" height="20" viewBox="0 0 120 24" aria-label="Five stars"><use href="#star" x="0"/><use href="#star" x="24"/><use href="#star" x="48"/><use href="#star" x="72"/><use href="#star" x="96"/></svg>
        “Simply the best”
      </li>
      <li class="review-list__item">
        <svg class="review-list__stars" width="96" height="20" viewBox="0 0 120 24" aria-label="Five stars"><use href="#star" x="0"/><use href="#star" x="24"/><use href="#star" x="48"/><use href="#star" x="72"/><use href="#star" x="96"/></svg>
        “Respectful and caring”
      </li>
      <li class="review-list__item">
        <svg class="review-list__stars" width="96" height="20" viewBox="0 0 120 24" aria-label="Five stars"><use href="#star" x="0"/><use href="#star" x="24"/><use href="#star" x="48"/><use href="#star" x="72"/><use href="#star" x="96"/></svg>
        “I wouldn’t go with anyone else!”
      </li>
    </ul>

    <blockquote class="testimonial">
      <span class="testimonial__line">“When life</span>
      <span class="testimonial__line">gets challenging</span>
      <span class="testimonial__line testimonial__line--accent">You want Marcus</span>
      <span class="testimonial__line">on your team!”</span>
    </blockquote>

    <div class="review-badge">
      <span class="review-badge__name">Starvu</span>
      <div class="review-badge__row">
        <span class="review-badge__label">Reviews</span>
        <svg width="120" height="24" viewBox="0 0 120 24" aria-label="Five stars"><use href="#star" x="0"/><use href="#star" x="24"/><use href="#star" x="48"/><use href="#star" x="72"/><use href="#star" x="96"/></svg>
      </div>
    </div>

    <div class="gavel-art" role="img" aria-label="Wooden judge's gavel with brass bands"></div>
  </main>
</body>
</html>
```